FEN Company Folder Design Color

I am looking for someone who can create a company folder design. F.E.N. Enterprises is a consulting firm, we assist business owner in their journeys to success. The design should be professional and mus include some inspirational words. I like elegance and modern. The colors red, white and black should be used. The design should look conservative, but not too serious. I do not like english or Times New Roman letters.

Target Market(s)

Healthcare Providers

Industry/Entity Type

Business

Colors
ec1f27
ffffff

Requirements
Must have
• color red and words like knowledge, success, confidence

```html
<!DOCTYPE html>
<html lang="en">
<head>
<meta charset="utf-8">
<title>F.E.N. Enterprises – Company Folder</title>
<link rel="stylesheet" href="https://fonts.googleapis.com/css2?family=Crimson+Pro:wght@700&family=Arimo:wght@400;700&display=swap">
<style>
  :root{
    --red:#ec1f27;
    --white:#ffffff;
    --sky:#2fa8e6;
    --navy:#1d4f86;
    --ground:#e6e6e6;
  }
  *{margin:0;padding:0;box-sizing:border-box}
  html,body{width:786px;height:1200px;overflow:hidden;background:var(--ground)}
  .canvas{position:relative;width:786px;height:1200px}
  .shapes{position:absolute;left:0;top:0}

  .brand{position:absolute;text-align:center;line-height:1;font-family:Arimo,Arial,sans-serif;font-weight:700;white-space:nowrap}
  .brand .dot{display:block;margin:0 auto 8px;border-radius:50%}
  .brand--back{left:135px;top:420px;width:130px;color:var(--white);font-size:11px}
  .brand--back .dot{width:32px;height:32px;background:var(--white)}
  .brand--front{left:560px;top:68px;width:200px;color:var(--red);font-size:16px}
  .brand--front .dot{width:44px;height:44px;background:var(--red);margin-bottom:12px}

  .contact{position:absolute;left:290px;top:424px;color:var(--white);font-family:Arimo,Arial,sans-serif;font-weight:700;font-size:7.5px;line-height:9.4px;white-space:nowrap}
  .contact .gap{height:7px}

  .flap-url{position:absolute;left:128px;top:515px;width:319px;text-align:center;color:var(--white);font-family:Arimo,Arial,sans-serif;font-weight:700;font-size:7.5px;transform:rotate(180deg)}

  .slogan{position:absolute;left:447px;top:232px;width:193px;height:91px;background:rgba(29,79,134,.72);color:var(--white);font-family:"Crimson Pro",Georgia,serif;font-weight:700;font-size:21px;line-height:24px;padding:10px 0 0 14px;letter-spacing:.3px}

  .about{position:absolute;left:66px;top:661px;width:296px;color:var(--white);font-family:Arimo,Arial,sans-serif}
  .about h2{font-size:13px;font-weight:700;margin-bottom:7px}
  .about p{font-size:8.1px;font-weight:700;line-height:10.6px}
</style>
</head>
<body>
<div class="canvas">
  <svg class="shapes" width="786" height="1200" viewBox="0 0 786 1200">
    <defs>
      <linearGradient id="backRed" x1="0" y1="0" x2="1" y2="1">
        <stop offset="0" stop-color="#e51a22"/>
        <stop offset=".5" stop-color="#ec2a31"/>
        <stop offset="1" stop-color="#e01820"/>
      </linearGradient>
      <linearGradient id="glassSky" x1="0" y1="0" x2="1" y2="1">
        <stop offset="0" stop-color="#1f74b8"/>
        <stop offset=".5" stop-color="#4fb2ea"/>
        <stop offset="1" stop-color="#bfe6fa"/>
      </linearGradient>
      <linearGradient id="coastSky" x1="0" y1="0" x2="0" y2="1">
        <stop offset="0" stop-color="#2fa6e4"/>
        <stop offset=".55" stop-color="#58bdef"/>
        <stop offset="1" stop-color="#2c9fdc"/>
      </linearGradient>
      <linearGradient id="frontPaper" x1="0" y1="0" x2="1" y2="0">
        <stop offset="0" stop-color="#ffffff"/>
        <stop offset="1" stop-color="#e9e9e9"/>
      </linearGradient>
    </defs>

    <polygon class="side-flap" points="44,48 128,38 128,497 44,487" fill="var(--red)"/>
    <rect class="back-cover" x="128" y="38" width="319" height="459" fill="url(#backRed)" role="img" aria-label="Red-toned photo of a glass office tower against the sky"/>
    <polygon class="bottom-flap" points="128,497 447,497 447,540 430,562 145,562 128,540" fill="var(--red)"/>

    <rect class="front-cover" x="447" y="38" width="315" height="459" fill="url(#frontPaper)"/>
    <path class="front-corner" d="M447,38 L470,38 Q452,70 447,130 Z" fill="var(--red)"/>
    <path class="front-photo" d="M447,112 C540,105 640,170 762,215 L762,232 C740,330 600,430 447,458 Z" fill="url(#glassSky)" role="img" aria-label="Photo of a glass office tower reflecting blue sky and clouds"/>
    <path class="front-stripe" d="M447,468 C610,440 738,345 762,244 L762,262 C738,362 620,458 447,484 Z" fill="var(--sky)"/>
    <path class="front-base" d="M447,497 L447,492 C632,466 745,372 762,272 L762,497 Z" fill="var(--red)"/>

    <rect class="inside-left" x="44" y="633" width="322" height="458" fill="url(#coastSky)" role="img" aria-label="Blue-toned photo of high-rise towers along a beach"/>
    <rect class="inside-right" x="366" y="633" width="306" height="458" fill="var(--white)"/>
    <rect class="inside-edge" x="672" y="633" width="90" height="458" fill="var(--red)"/>
    <polygon class="pocket-flap" points="366,1091 672,1091 672,1144 654,1163 384,1163 366,1144" fill="var(--red)"/>
  </svg>

  <div class="brand brand--back">
    <span class="dot"></span>
    F.E.N. Enterprises
  </div>

  <div class="contact">
    <div>P. 555.014.2290</div>
    <div>F. 555.014.7731</div>
    <div>www.fenhealthconsulting.com</div>
    <div class="gap"></div>
    <div>2480 N. Orchard Road</div>
    <div>Riverton, TX 75010</div>
  </div>

  <div class="flap-url">www.fenhealthconsulting.com</div>

  <div class="brand brand--front">
    <span class="dot"></span>
    F.E.N. Enterprises
  </div>

  <div class="slogan">KNOWLEDGE<br>CONFIDENCE<br>SUCCESS</div>

  <div class="about">
    <h2>About Us</h2>
    <p>FEN Enterprises has been assisting clients for more than 20 years. Most of the clients we serve are throughout Texas. FEN Enterprises has a team of experts who are hands on consultants. We go in your agency, pick up our sleeves and work.</p>
  </div>
</div>
</body>
</html>
```